Designer and consultant for professionals/businesses and manufacturers in the kitchen and bath in...

I have 30 years of design experience, and 19 of those years within the marketing team of a national cabinet manufacturer. This role gave me the opportunity to consult and design for kitchen/bath businesses, from boutique to multi-store national scale. My services include layout and spatial planning, individual display design, and product design for cabinet manufacturers. From showrooms, to trade shows to integrated design collections. I would like to see designs that convey professionalism, as well as an appeal to the creative designer mind!

Target Market(s)

Kitchen and bath dealers, as well as mid-scale multi-store home centers. Cabinet manufacturers, Trade Show agencies.

Industry/Entity Type

Kitchen

Contact Information for Business Card

Serving Kitchen and Bath Businesses

Logo Text

MT (initials for business name)

Font styles to use
Serif
Sans Serif
Decorative

Colors
e34197

Requirements
Must have
• Marlowe Tavish Design and Consulting, Inc. (business name)
• marlowe@mtvantra.com (email)
• 917-555-0148 (phone)
• mtvantra.com (website)
Nice to have
• Inclusions of geometric shapes; particularly a 30/15 degree triangle and circle(s)
• 2 colors
Should not have
• Not too artsy!

```html
<!DOCTYPE html>
<html lang="en">
<head>
<meta charset="utf-8">
<title>Marlowe Tavish Design and Consulting — Business Card</title>
<link rel="stylesheet" href="https://fonts.googleapis.com/css2?family=Courier+Prime:wght@400;700&family=Tinos:wght@700&display=swap">
<style>
  :root {
    --page: #ffffff;
    --card-grey: #c9cac9;
    --card-light: #ededed;
    --band-grey: #a3a3a3;
    --ink: #2f2a2a;
    --accent: #e8598f;
  }
  html, body {
    margin: 0;
    padding: 0;
    width: 1200px;
    height: 903px;
    overflow: hidden;
    background: var(--page);
  }
  .sheet {
    position: relative;
    width: 1200px;
    height: 903px;
  }
  .card { position: absolute; display: block; }
  .card--front { left: 0; top: 0; width: 570px; height: 363px; }
  .card--back { left: 617px; top: 541px; width: 583px; height: 362px; }
  .company-name {
    font-family: "Courier Prime", "Courier New", monospace;
    font-size: 46px;
    fill: var(--ink);
  }
  .contact-line {
    font-family: "Courier Prime", "Courier New", monospace;
    font-size: 22px;
    fill: var(--ink);
  }
  .contact-phone {
    font-family: "Tinos", "Times New Roman", serif;
    font-weight: 700;
    font-size: 22px;
    fill: var(--ink);
  }
  .monogram {
    font-family: "Courier Prime", "Courier New", monospace;
    font-weight: 700;
    fill: var(--accent);
  }
</style>
</head>
<body>
<main class="sheet">

  <svg class="card card--front" viewBox="0 0 570 363" xmlns="http://www.w3.org/2000/svg" aria-label="Business card front">
    <rect class="card-base" x="0" y="0" width="570" height="363" fill="var(--card-grey)"/>
    <path class="card-panel" fill="var(--card-light)"
          d="M0 161 C40 110 95 55 155 19 L570 20 L570 234 C545 280 515 315 481 344 L0 343 Z"/>
    <text class="monogram" x="486" y="118" font-size="84" text-anchor="middle">MT</text>
    <text class="company-name" x="19" y="161" textLength="401" lengthAdjust="spacingAndGlyphs">Marlowe Tavish Design and Consulting, Inc</text>
    <text class="contact-line contact-email" x="26" y="202" textLength="274" lengthAdjust="spacing">marlowe@mtvantra.com</text>
    <text class="contact-phone" x="28" y="237" textLength="217" lengthAdjust="spacing">917-555-0148</text>
    <text class="contact-line contact-web" x="29" y="266" textLength="226" lengthAdjust="spacing">mtvantra.com</text>
  </svg>

  <svg class="card card--back" viewBox="0 0 583 362" xmlns="http://www.w3.org/2000/svg" aria-label="Business card back">
    <defs>
      <clipPath id="back-shape">
        <rect x="0" y="0" width="583" height="362" rx="10" ry="10"/>
      </clipPath>
    </defs>
    <g clip-path="url(#back-shape)">
      <rect class="card-base" x="0" y="0" width="583" height="362" fill="var(--card-grey)"/>
      <polygon class="diagonal-band" fill="var(--band-grey)" points="366,0 583,0 583,10 124,362 1,362"/>
      <circle class="emblem-disc" cx="226" cy="169" r="127" fill="var(--card-light)" stroke="var(--band-grey)" stroke-width="13"/>
      <text class="monogram" x="226" y="198" font-size="90" text-anchor="middle">MT</text>
    </g>
  </svg>

</main>
</body>
</html>
```